Dental Office Looking for Modern, simple business cards

We just acquired our logo. Now we would like to make business cards. We are a dental office with two doctors. We are husband and wife and have a small boutique dental practice in a small town. We love our patients and they are always asking us to give our business cards to their friends. Please help us make business cards :-)

Target Market(s)

30-60 yr old

Industry/Entity Type

Dental Clinic

Contact Information for Business Card

Birch Hollow Dental P.C.
Family and Cosmetic Dentistry
4826 Delmore Rd. Schenectady NY 12417
Tel: 518 642 7731 Fax: 518 642 7048

Dr. Tomas K. Brellin DDS
Dr. Marisol Ede Thornquist DDS

Font styles to use
Serif
Sans Serif

Requirements
Must have
• Simple clean design, modern, colorful. Should incorporate the logo.
Nice to have
• dental imagery ( teeth, smile, etc ...).

```html
<!DOCTYPE html>
<html lang="en">
<head>
<meta charset="utf-8">
<title>Birch Hollow Dental – Business Cards</title>
<link rel="stylesheet" href="https://fonts.googleapis.com/css2?family=Cinzel:wght@600&family=Marcellus&family=Roboto:wght@400;500&display=swap">
<style>
  :root {
    --stage: #1f1f1f;
    --card-dark: #141414;
    --card-blue: #1f7cc6;
    --card-blue-light: #2b8ad0;
    --brand-blue: #2a7fcb;
    --brand-grey: #8a8d91;
    --white: #ffffff;
  }
  * { margin: 0; padding: 0; box-sizing: border-box; }
  html, body {
    width: 1200px;
    height: 1200px;
    overflow: hidden;
    background: var(--stage);
  }
  .sheet {
    width: 1200px;
    height: 1200px;
    display: flex;
    flex-direction: column;
    align-items: center;
    justify-content: center;
    gap: 44px;
  }
  .card {
    width: 900px;
    height: 514px;
    position: relative;
    overflow: hidden;
    box-shadow: 0 18px 40px rgba(0,0,0,0.55);
  }
  .brand-lockup {
    display: flex;
    align-items: center;
    justify-content: center;
    gap: 16px;
  }
  .brand-dot {
    width: 40px;
    height: 40px;
    border-radius: 50%;
    flex: none;
  }
  .brand-name {
    font-family: "Cinzel", serif;
    font-weight: 600;
    letter-spacing: 1px;
    line-height: 1;
  }
  .tagline {
    font-family: "Marcellus", serif;
    font-size: 25px;
    letter-spacing: 0.5px;
    text-align: center;
  }

  /* Back side */
  .card--back {
    background: var(--card-dark);
    display: flex;
    flex-direction: column;
    align-items: center;
    justify-content: center;
    gap: 16px;
  }
  .card--back .brand-dot { background: var(--brand-grey); }
  .card--back .brand-name { color: var(--brand-blue); font-size: 48px; }
  .card--back .tagline { color: var(--brand-blue); }

  /* Front side */
  .card--front {
    background: linear-gradient(160deg, var(--card-blue-light) 0%, var(--card-blue) 60%);
    color: var(--white);
  }
  .mark-area {
    position: absolute;
    left: 0;
    top: 0;
    width: 400px;
    height: 514px;
    background: linear-gradient(135deg, rgba(255,255,255,0.30) 0%, rgba(255,255,255,0.12) 100%);
  }
  .front-brand {
    position: absolute;
    top: 110px;
    left: 420px;
    right: 40px;
  }
  .front-brand .brand-dot { width: 34px; height: 34px; background: var(--white); }
  .front-brand .brand-name { font-size: 38px; color: var(--white); }
  .front-brand .tagline { margin-top: 14px; font-size: 22px; color: var(--white); }
  .contact {
    position: absolute;
    left: 440px;
    top: 285px;
    font-family: "Roboto", sans-serif;
  }
  .doctors { font-weight: 500; font-size: 24px; line-height: 1.35; margin-bottom: 16px; }
  .contact-list { list-style: none; font-size: 21px; line-height: 1.55; }
  .contact-list li { display: flex; align-items: center; gap: 12px; }
  .contact-icon { width: 22px; height: 22px; flex: none; }
</style>
</head>
<body>
<main class="sheet">
  <section class="card card--back" aria-label="Card back">
    <div class="brand-lockup">
      <span class="brand-dot" aria-hidden="true"></span>
      <div class="brand-name">Birch Hollow Dental</div>
    </div>
    <div class="tagline">Family and Cosmetic Dentistry</div>
  </section>

  <section class="card card--front" aria-label="Card front">
    <div class="mark-area" role="img" aria-label="Large brand mark decoration"></div>
    <div class="front-brand">
      <div class="brand-lockup">
        <span class="brand-dot" aria-hidden="true"></span>
        <div class="brand-name">Birch Hollow Dental</div>
      </div>
      <div class="tagline">Family and Cosmetic Dentistry</div>
    </div>
    <div class="contact">
      <p class="doctors">Dr. Tomas K. Brellin<br>Dr. Marisol Ede Thornquist</p>
      <ul class="contact-list">
        <li>
          <svg class="contact-icon" viewBox="0 0 24 24" aria-hidden="true">
            <circle cx="12" cy="12" r="12" fill="#fff"/>
            <path d="M8.2 6.5l2 2.1-1.1 1.6c.8 1.7 2 2.9 3.7 3.7l1.6-1.1 2.1 2-1.2 2c-4.4-.4-8-4-8.3-8.4z" fill="#1f7cc6"/>
          </svg>
          <span>518 642 7731</span>
        </li>
        <li>
          <svg class="contact-icon" viewBox="0 0 24 24" aria-hidden="true">
            <circle cx="12" cy="12" r="12" fill="#fff"/>
            <rect x="8.5" y="6" width="7" height="4" fill="#1f7cc6"/>
            <rect x="6" y="10" width="12" height="5.5" rx="1" fill="#1f7cc6"/>
            <rect x="8.5" y="13.5" width="7" height="4.5" fill="#1f7cc6" stroke="#fff" stroke-width="1"/>
          </svg>
          <span>518 642 7048</span>
        </li>
        <li>
          <svg class="contact-icon" viewBox="0 0 24 24" aria-hidden="true">
            <circle cx="12" cy="12" r="12" fill="#fff"/>
            <path d="M12 5.5a4.5 4.5 0 0 0-4.5 4.5c0 3.3 4.5 8.5 4.5 8.5s4.5-5.2 4.5-8.5A4.5 4.5 0 0 0 12 5.5z" fill="#1f7cc6"/>
            <circle cx="12" cy="10" r="1.7" fill="#fff"/>
          </svg>
          <span>4826 Delmore Rd. Schenectady NY 12417</span>
        </li>
      </ul>
    </div>
  </section>
</main>
</body>
</html>
```